International games company requires localisation design of gfa prediction game.

Using our current designs and those of our competitors, Brightwater Play are looking for novel design work that refreshes, enlivens and brings our games in line with what is expected in the American market. The Sports lottery game works by users selecting a winning margin for a series of 8 (in this case) GFA games. Should all of these predictions be correct, the user wins the jackpot.We are a software developer that creates free-to-play games specialised for the iGaming industry which function as customer acquisition and retention tools. Our user acquisition and retention models and processes are differentiated from our competitors by being driven by our unique style and application of gamification techniques and user behaviour analysis. Designs submitted should take inspiration from the attached images but designers should feel free to add their own flair and creativity whilst embracing intuitive UX and UI design principles.

Target Market(s)

American Sports fans aged 18+

Font styles to use
Sans Serif

Colors

Designer to choose colors to be used in the design.

Requirements
Must have
• User-friendly, intelligent design, applicable to being recoloured and branded to fit client's brands.

```html
<!DOCTYPE html>
<html lang="en">
<head>
<meta charset="utf-8">
<title>GFA Prediction Game – Parlay Summary</title>
<link rel="stylesheet" href="https://fonts.googleapis.com/css2?family=Open+Sans:wght@400;600;700;800&display=swap">
<style>
  :root {
    --ink: #111111;
    --ink-soft: #444444;
    --black: #000000;
    --sun: #f3c84f;
    --navy: #1b1d3f;
    --navy-nav: #272a52;
    --green: #2fbf71;
    --green-text: #2aa860;
    --line: #9a9a9a;
    --paper: #ffffff;
    --book-blue: #2c4f8c;
    --gold-line: #e2b04a;
    --team-purple: #6a45cc;
    --team-gold: #f2b829;
    --team-aqua: #3fd3d3;
    --team-red: #ec3a24;
  }
  * { box-sizing: border-box; margin: 0; padding: 0; }
  html, body {
    width: 1200px; height: 2533px; overflow: hidden;
    background: var(--paper);
    font-family: "Open Sans", Arial, sans-serif;
    color: var(--ink);
  }
  .screen { position: relative; width: 1200px; height: 2533px; overflow: hidden; }

  .status-bar { position: absolute; left: 0; top: 0; width: 1200px; height: 98px; background: var(--black); }

  .confirm-bar { position: absolute; left: 0; top: 98px; width: 1200px; height: 184px; background: var(--sun); }
  .back-button {
    position: absolute; left: 22px; top: 58px; width: 85px; height: 84px;
    background: var(--navy); border: 3px solid #000; border-radius: 8px;
    display: flex; align-items: center; justify-content: center;
  }
  .confirm-text { position: absolute; left: 183px; top: 36px; font-size: 44px; line-height: 56px; }
  .confirm-text strong { font-weight: 700; display: block; }
  .confirm-text span { font-weight: 600; }

  .returns-title {
    position: absolute; top: 305px; left: 0; width: 1200px; text-align: center;
    font-size: 46px; line-height: 56px; font-weight: 700; color: var(--ink-soft);
  }

  .odds-head { position: absolute; top: 490px; left: 0; width: 1200px; height: 50px; font-size: 36px; font-weight: 700; }
  .odds-head span { position: absolute; top: 0; }
  .odds-head .offers { color: var(--green-text); }

  .odds-row { position: absolute; left: 0; width: 1200px; height: 90px; }
  .bookmaker {
    position: absolute; left: 64px; top: 0; width: 260px; height: 90px;
    border: 2px solid #8a8a8a; border-radius: 4px;
    display: flex; align-items: center; justify-content: center;
    font-size: 34px; font-weight: 600; color: var(--book-blue);
  }
  .odds-row .odds, .odds-row .win {
    position: absolute; top: 22px; font-size: 36px; font-weight: 700;
  }
  .odds-row .odds { left: 392px; }
  .odds-row .win { left: 792px; }
  .offer-info { position: absolute; left: 617px; top: 10px; width: 70px; height: 70px; }
  .bet-button {
    position: absolute; left: 975px; top: 5px; width: 177px; height: 80px;
    background: var(--green); color: #fff; border-radius: 4px;
    font-size: 36px; font-weight: 600;
    display: flex; align-items: center; justify-content: center;
  }

  .predictions-band { position: absolute; left: 0; top: 1149px; width: 1200px; height: 195px; background: var(--navy); }
  .predictions-band h2 {
    position: absolute; left: 64px; top: 68px; font-size: 44px; font-weight: 700; color: #fff; letter-spacing: 0.5px;
  }
  .predictions-band .include {
    position: absolute; right: 70px; top: 68px; font-size: 44px; font-weight: 700; color: #fff;
  }
  .predictions-band .rule { position: absolute; left: 44px; top: 148px; width: 1094px; height: 3px; background: var(--gold-line); }

  .prediction-list { position: absolute; left: 0; top: 1344px; width: 1200px; height: 989px; overflow: hidden; }
  .prediction { position: relative; height: 219px; }
  .prediction::after {
    content: ""; position: absolute; left: 44px; right: 54px; bottom: 0; height: 2px; background: var(--line);
  }
  .team-tile {
    position: absolute; top: 48px; width: 168px; height: 170px;
    border: 2px solid #555; border-radius: 4px; background: #fff;
    padding: 14px;
  }
  .team-tile.home { left: 47px; }
  .team-tile.away { left: 300px; }
  .team-swatch { width: 100%; height: 100%; border-radius: 3px; }
  .team-swatch.purple { background: var(--team-purple); }
  .team-swatch.gold { background: var(--team-gold); }
  .team-swatch.aqua { background: var(--team-aqua); }
  .team-swatch.red { background: var(--team-red); }
  .pick { position: absolute; left: 520px; top: 102px; font-size: 44px; font-weight: 700; letter-spacing: 0.5px; white-space: nowrap; }
  .price { position: absolute; left: 910px; top: 104px; font-size: 44px; font-weight: 700; }
  .include-check {
    position: absolute; left: 1064px; top: 88px; width: 88px; height: 88px;
    background: var(--green); border-radius: 6px;
    display: flex; align-items: center; justify-content: center;
  }

  .bottom-nav { position: absolute; left: 0; top: 2333px; width: 1200px; height: 200px; background: var(--navy-nav); }
  .nav-item {
    position: absolute; top: 28px; width: 200px; margin-left: -100px; text-align: center;
    color: #fff; font-size: 34px; font-weight: 400;
  }
  .nav-item svg { display: block; margin: 0 auto 14px; }
</style>
</head>
<body>
<main class="screen">
  <div class="status-bar"></div>

  <header class="confirm-bar">
    <div class="back-button">
      <svg width="40" height="50" viewBox="0 0 40 50"><polyline points="28,6 10,25 28,44" fill="none" stroke="#fff" stroke-width="4"/></svg>
    </div>
    <p class="confirm-text"><strong>Job done.</strong><span>Your predictions have been entered.</span></p>
  </header>

  <h1 class="returns-title">Based on your predictions,<br>a $10 parlay would return...</h1>

  <div class="odds-head">
    <span style="left:64px">BOOKMAKER</span>
    <span style="left:400px">ODDS</span>
    <span class="offers" style="left:598px">OFFERS</span>
    <span style="left:815px">WIN</span>
  </div>

  <div class="odds-row" style="top:594px">
    <div class="bookmaker">Harborline</div>
    <span class="odds">+4100</span>
    <svg class="offer-info" viewBox="0 0 70 70"><circle cx="35" cy="35" r="31" fill="none" stroke="#2aa860" stroke-width="4"/><circle cx="35" cy="21" r="4" fill="#2aa860"/><rect x="32" y="30" width="6" height="24" fill="#2aa860"/></svg>
    <span class="win">$41000</span>
    <div class="bet-button">Bet</div>
  </div>
  <div class="odds-row" style="top:697px">
    <div class="bookmaker">Harborline</div>
    <span class="odds">+3900</span>
    <svg class="offer-info" viewBox="0 0 70 70"><circle cx="35" cy="35" r="31" fill="none" stroke="#2aa860" stroke-width="4"/><circle cx="35" cy="21" r="4" fill="#2aa860"/><rect x="32" y="30" width="6" height="24" fill="#2aa860"/></svg>
    <span class="win">$39000</span>
    <div class="bet-button">Bet</div>
  </div>
  <div class="odds-row" style="top:800px">
    <div class="bookmaker">Harborline</div>
    <span class="odds">+3500</span>
    <svg class="offer-info" viewBox="0 0 70 70"><circle cx="35" cy="35" r="31" fill="none" stroke="#2aa860" stroke-width="4"/><circle cx="35" cy="21" r="4" fill="#2aa860"/><rect x="32" y="30" width="6" height="24" fill="#2aa860"/></svg>
    <span class="win">$35000</span>
    <div class="bet-button">Bet</div>
  </div>
  <div class="odds-row" style="top:904px">
    <div class="bookmaker">Harborline</div>
    <span class="odds">+2100</span>
    <svg class="offer-info" viewBox="0 0 70 70"><circle cx="35" cy="35" r="31" fill="none" stroke="#2aa860" stroke-width="4"/><circle cx="35" cy="21" r="4" fill="#2aa860"/><rect x="32" y="30" width="6" height="24" fill="#2aa860"/></svg>
    <span class="win">$21000</span>
    <div class="bet-button">Bet</div>
  </div>

  <section class="predictions-band">
    <h2>YOUR PREDICTIONS</h2>
    <span class="include">INCLUDE</span>
    <div class="rule"></div>
  </section>

  <section class="prediction-list">
    <div class="prediction">
      <div class="team-tile home"><div class="team-swatch purple" role="img" aria-label="Vandals team badge"></div></div>
      <div class="team-tile away"><div class="team-swatch gold" role="img" aria-label="Foresters team badge"></div></div>
      <span class="pick">Vandals to win</span><span class="price">-1200</span>
      <div class="include-check"><svg width="54" height="44" viewBox="0 0 54 44"><polyline points="6,22 20,36 48,8" fill="none" stroke="#fff" stroke-width="7"/></svg></div>
    </div>
    <div class="prediction">
      <div class="team-tile home"><div class="team-swatch aqua" role="img" aria-label="Tidecats team badge"></div></div>
      <div class="team-tile away"><div class="team-swatch red" role="img" aria-label="Opponent team badge"></div></div>
      <span class="pick">Tidecat to win</span><span class="price">-150</span>
      <div class="include-check"><svg width="54" height="44" viewBox="0 0 54 44"><polyline points="6,22 20,36 48,8" fill="none" stroke="#fff" stroke-width="7"/></svg></div>
    </div>
    <div class="prediction">
      <div class="team-tile home"><div class="team-swatch purple" role="img" aria-label="Vandals team badge"></div></div>
      <div class="team-tile away"><div class="team-swatch gold" role="img" aria-label="Foresters team badge"></div></div>
      <span class="pick">Vandals to win</span><span class="price">-1200</span>
      <div class="include-check"><svg width="54" height="44" viewBox="0 0 54 44"><polyline points="6,22 20,36 48,8" fill="none" stroke="#fff" stroke-width="7"/></svg></div>
    </div>
    <div class="prediction">
      <div class="team-tile home"><div class="team-swatch aqua" role="img" aria-label="Tidecats team badge"></div></div>
      <div class="team-tile away"><div class="team-swatch red" role="img" aria-label="Opponent team badge"></div></div>
      <span class="pick">Tidecat to win</span><span class="price">-150</span>
      <div class="include-check"><svg width="54" height="44" viewBox="0 0 54 44"><polyline points="6,22 20,36 48,8" fill="none" stroke="#fff" stroke-width="7"/></svg></div>
    </div>
    <div class="prediction">
      <div class="team-tile home"><div class="team-swatch purple" role="img" aria-label="Vandals team badge"></div></div>
      <div class="team-tile away"><div class="team-swatch gold" role="img" aria-label="Foresters team badge"></div></div>
      <span class="pick">Vandals to win</span><span class="price">-1200</span>
      <div class="include-check"><svg width="54" height="44" viewBox="0 0 54 44"><polyline points="6,22 20,36 48,8" fill="none" stroke="#fff" stroke-width="7"/></svg></div>
    </div>
  </section>

  <nav class="bottom-nav">
    <div class="nav-item" style="left:196px">
      <svg width="80" height="80" viewBox="0 0 80 80" fill="none" stroke="#fff" stroke-width="3.5">
        <circle cx="58" cy="16" r="9"/><circle cx="20" cy="40" r="9"/><circle cx="58" cy="64" r="9"/>
        <line x1="28" y1="35" x2="50" y2="21"/><line x1="28" y1="45" x2="50" y2="59"/>
      </svg>Share
    </div>
    <div class="nav-item" style="left:622px">
      <svg width="80" height="80" viewBox="0 0 80 80" fill="none" stroke="#fff" stroke-width="3.5">
        <path d="M40 14 H14 V68 H66 V40"/><path d="M60 8 L72 20 L40 52 L28 54 L30 42 Z"/>
      </svg>Edit
    </div>
    <div class="nav-item" style="left:1007px">
      <svg width="80" height="80" viewBox="0 0 80 80" fill="none" stroke="#fff" stroke-width="3.5">
        <path d="M8 38 L40 10 L72 38"/><path d="M16 32 V72 H64 V32"/><path d="M32 72 V50 H48 V72"/>
      </svg>Home
    </div>
  </nav>
</main>
</body>
</html>
```